Mortgage Broking boutique Business

I’m wanting a revamped look to my existing business card design. I do like the black and silver but happy to have other colours introduced based on your creation. I’ve attached a copy of my current card so you can have a starting point updated details noted brloe. I deal with high net worth individuals so need my card to be sophisticated, classy that gives off a classy vibe

Target Market(s)

High net worth, wealthy

Industry/Entity Type

Mortgage Brokerage

Contact Information for Business Card

Job title: Finance Executive
Phone: +61 7 3287 4419
Mobile: 0471 352 608
Email: marcus@quillbrookcapital.com.au
Web: www.quillbrookcapital.com.au
Address: level 36 Tindale Court, 58 Harwick St Brisbane QLD 4000

Font styles to use
Other font styles liked:
• Helvetica

Colors

Designer to choose colors to be used in the design.

Requirements
Must have
• Use my existing card design as a starting point

```html
<!DOCTYPE html>
<html lang="en">
<head>
<meta charset="utf-8">
<title>Quillbrook Capital – Business Card</title>
<link href="https://fonts.googleapis.com/css2?family=Open+Sans:wght@300;400;700&display=swap" rel="stylesheet">
<style>
  :root {
    --page: #e6e7e9;
    --ink: #111111;
    --charcoal: #2a2a2a;
    --black: #0b0b0b;
    --white: #ffffff;
    --silver: #b9b9b9;
    --silver-light: #e2e2e2;
    --grey-text: #6d6d6d;
    --grey-soft: #9a9a9a;
    --icon: #a8a8a8;
  }
  * { box-sizing: border-box; margin: 0; padding: 0; }
  html, body {
    width: 1200px; height: 900px; overflow: hidden;
    background: var(--page);
    font-family: "Open Sans", Arial, sans-serif;
  }
  .sheet {
    width: 1200px; height: 900px;
    display: flex; align-items: center; justify-content: center; gap: 40px;
  }
  .card {
    position: relative; width: 540px; height: 310px;
    border-radius: 22px; overflow: hidden;
    box-shadow: 0 8px 24px rgba(0,0,0,.18);
  }

  /* Front */
  .card--front { background: var(--white); }
  .card__edge {
    position: absolute; inset: 0;
    background: var(--silver-light);
  }
  .card__face {
    position: absolute; top: 12px; left: 0; right: 12px; bottom: 46px;
    background: var(--white);
    border-top-right-radius: 14px;
  }
  .brand {
    position: absolute; left: 40px; top: 88px;
    color: var(--charcoal); font-weight: 300; text-transform: uppercase;
    line-height: 1.15;
  }
  .brand__main { display: block; font-size: 26px; letter-spacing: 6px; }
  .brand__sub { display: block; font-size: 14px; letter-spacing: 6px; padding-left: 44px; }
  .divider {
    position: absolute; left: 292px; top: 36px; width: 1px; height: 170px;
    background: linear-gradient(var(--white), var(--silver), var(--white));
  }
  .contact { position: absolute; left: 312px; top: 72px; }
  .contact__name { font-size: 17px; font-weight: 700; color: var(--ink); }
  .contact__title { font-size: 11px; font-weight: 300; color: var(--grey-soft); margin-bottom: 8px; }
  .contact__row {
    display: flex; align-items: center; gap: 5px;
    font-size: 10.5px; color: var(--grey-text); line-height: 17px; white-space: nowrap;
  }
  .contact__row svg { width: 11px; height: 11px; flex: none; }
  .contact__gap { width: 8px; }
  .address-band {
    position: absolute; left: 0; right: 0; bottom: 0; height: 46px;
    background: var(--black);
    color: var(--white); font-weight: 700; font-size: 15px;
    display: flex; align-items: center; padding-left: 30px;
  }

  /* Back */
  .card--back { background: radial-gradient(ellipse at 55% 40%, #333 0%, #151515 55%, #060606 100%); }
  .back-brand {
    position: absolute; left: 0; right: 0; top: 92px; text-align: center;
    color: var(--white); font-weight: 300; text-transform: uppercase; line-height: 1.2;
  }
  .back-brand .brand__main { font-size: 38px; letter-spacing: 9px; }
  .back-brand .brand__sub { font-size: 18px; letter-spacing: 8px; padding-left: 0; }
  .web-band {
    position: absolute; left: 0; right: 0; bottom: 0; height: 40px;
    background: linear-gradient(var(--silver-light), var(--silver));
    color: var(--charcoal); font-size: 15px; font-weight: 400;
    display: flex; align-items: center; padding-left: 34px;
  }
</style>
</head>
<body>
<main class="sheet">

  <section class="card card--front" aria-label="Card front">
    <div class="card__edge" role="img" aria-label="Fine silver line texture along the top and right edge"></div>
    <div class="card__face">
      <div class="brand">
        <span class="brand__main">Quillbrook</span>
        <span class="brand__sub">Capital</span>
      </div>
      <div class="divider"></div>
      <div class="contact">
        <p class="contact__name">Example Name</p>
        <p class="contact__title">Finance Executive</p>
        <p class="contact__row">
          <svg viewBox="0 0 12 12"><circle cx="6" cy="6" r="6" fill="var(--icon)"/><path d="M4 3.2l1 1.4-.6.8c.4.8 1 1.4 1.8 1.8l.8-.6 1.4 1-.6 1.2C5.5 8.6 3.4 6.5 3 4z" fill="#fff"/></svg>
          +61 7 3287 4419
          <span class="contact__gap"></span>
          <svg viewBox="0 0 12 12"><circle cx="6" cy="6" r="6" fill="var(--icon)"/><rect x="4.2" y="2.6" width="3.6" height="6.8" rx=".6" fill="#fff"/></svg>
          0471 352 608
        </p>
        <p class="contact__row">
          <svg viewBox="0 0 12 12"><circle cx="6" cy="6" r="6" fill="var(--icon)"/><rect x="3" y="4" width="6" height="4.2" fill="#fff"/><path d="M3 4l3 2.3L9 4" stroke="var(--icon)" stroke-width=".7" fill="none"/></svg>
          marcus@quillbrookcapital.com.au
        </p>
        <p class="contact__row">
          <svg viewBox="0 0 12 12"><circle cx="6" cy="6" r="6" fill="var(--icon)"/><circle cx="6" cy="6" r="3" fill="none" stroke="#fff" stroke-width=".8"/><path d="M3 6h6M6 3c-1.4 1.6-1.4 4.4 0 6M6 3c1.4 1.6 1.4 4.4 0 6" stroke="#fff" stroke-width=".6" fill="none"/></svg>
          www.quillbrookcapital.com.au
        </p>
      </div>
    </div>
    <div class="address-band">level 36 Tindale Court, 58 Harwick St Brisbane QLD 4000</div>
  </section>

  <section class="card card--back" aria-label="Card back">
    <div class="back-brand">
      <span class="brand__main">Quillbrook</span>
      <span class="brand__sub">Capital</span>
    </div>
    <div class="web-band">www.quillbrookcapital.com.au</div>
  </section>

</main>
</body>
</html>
```